Group Medical Practice needs stationery, business cards etc. designed

We need stationery designed for a multisite practice that offers primary medical, dental and behavioral healthcare. We would like a design that is consistent for letterhead, business cards, Microsoft Outlook stationery etc. We have attached our new logo design.

```html
<!DOCTYPE html>
<html lang="en">
<head>
<meta charset="utf-8">
<title>Ridgeline Health Partners – Letterhead</title>
<link rel="stylesheet" href="https://fonts.googleapis.com/css2?family=Arimo:wght@400&family=Pinyon+Script&display=swap">
<style>
  :root {
    --paper: #ffffff;
    --ink: #3a3a3a;
    --ink-soft: #4a4a4a;
    --brand-green: #8dc63f;
    --brand-blue: #1f7fc4;
    --wash-green: #eef5e0;
  }
  * { margin: 0; padding: 0; box-sizing: border-box; }
  html, body { width: 928px; height: 1200px; overflow: hidden; background: var(--paper); }
  .letterhead {
    position: relative;
    width: 928px;
    height: 1200px;
    background: var(--paper);
    font-family: "Arimo", Arial, sans-serif;
    color: var(--ink);
    overflow: hidden;
  }
  .brand-wash {
    position: absolute;
    left: 0; bottom: 0;
    width: 928px; height: 420px;
    background: linear-gradient(to top, var(--wash-green) 0%, rgba(238,245,224,0.6) 55%, rgba(238,245,224,0) 100%);
  }
  .contact-list {
    position: absolute;
    left: 48px; top: 30px;
    list-style: none;
    font-size: 9.5px;
    line-height: 12px;
    color: var(--ink);
  }
  .contact-list li { display: flex; align-items: flex-start; margin-bottom: 4px; }
  .contact-list svg { width: 11px; height: 11px; margin-right: 5px; flex: none; fill: var(--brand-green); }
  .contact-list .address { margin-bottom: 9px; }
  .brand-name {
    position: absolute;
    right: 24px; top: 86px;
    display: flex; align-items: center;
    font-size: 27px;
    color: var(--brand-blue);
    letter-spacing: 0.5px;
  }
  .brand-name .brand-dot {
    width: 16px; height: 16px; border-radius: 50%;
    background: var(--brand-green);
    margin-right: 10px;
  }
  .salutation {
    position: absolute;
    left: 74px; top: 234px;
    font-size: 15.6px;
  }
  .letter-body {
    position: absolute;
    left: 154px; top: 266px;
    width: 702px;
    font-size: 15.4px;
    line-height: 20.4px;
    color: var(--ink);
  }
  .letter-body p { margin-bottom: 20.4px; }
  .letter-body p.run-on { margin-top: -20.4px; }
  .sign-off {
    position: absolute;
    left: 106px; top: 842px;
    font-size: 15.6px;
    line-height: 20px;
    color: var(--ink-soft);
  }
  .signature {
    position: absolute;
    left: 78px; top: 898px;
    font-family: "Pinyon Script", cursive;
    font-size: 54px;
    line-height: 60px;
    color: #2b2b2b;
  }
  .signer-title {
    position: absolute;
    left: 106px; top: 970px;
    font-size: 15.6px;
    color: var(--ink-soft);
  }
</style>
</head>
<body>
<main class="letterhead">
  <div class="brand-wash" role="img" aria-label="Faint pale green brand decoration across the lower page"></div>

  <ul class="contact-list">
    <li class="address">
      <svg viewBox="0 0 12 12" aria-hidden="true"><path d="M6 0.5a3.8 3.8 0 0 0-3.8 3.8C2.2 7.2 6 11.5 6 11.5s3.8-4.3 3.8-7.2A3.8 3.8 0 0 0 6 0.5zm0 5.3a1.5 1.5 0 1 1 0-3 1.5 1.5 0 0 1 0 3z"/></svg>
      <span>412 Alder Lane Ste 204<br>Maple Hollow, Virginia 24000</span>
    </li>
    <li>
      <svg viewBox="0 0 12 12" aria-hidden="true"><path d="M2.4 0.8l2 2.2-1 1.4c.7 1.6 2 2.9 3.6 3.6l1.4-1 2.2 2-1.2 1.8C5.2 10.6 1.4 6.8 0.6 2z"/></svg>
      <span>000-000-0000</span>
    </li>
    <li>
      <svg viewBox="0 0 12 12" aria-hidden="true"><rect x="0.5" y="2.5" width="11" height="7.5"/></svg>
      <span>info@ridgelinehealth.com</span>
    </li>
    <li>
      <svg viewBox="0 0 12 12" aria-hidden="true"><path d="M6 0.5a5.5 5.5 0 1 0 0 11 5.5 5.5 0 0 0 0-11zm0 1.2c.8.8 1.3 2 1.5 3.6h-3c.2-1.6.7-2.8 1.5-3.6zM1.8 6.5h1.8c.1 1.2.4 2.3 1 3.1a4.3 4.3 0 0 1-2.8-3.1zm0-1.2a4.3 4.3 0 0 1 2.8-3.1c-.6.8-.9 1.9-1 3.1zm2.7 1.2h3c-.2 1.6-.7 2.8-1.5 3.6-.8-.8-1.3-2-1.5-3.6zm2.9 3.1c.6-.8.9-1.9 1-3.1h1.8a4.3 4.3 0 0 1-2.8 3.1zm1-4.3c-.1-1.2-.4-2.3-1-3.1a4.3 4.3 0 0 1 2.8 3.1z"/></svg>
      <span>www.ridgelinehealth.com</span>
    </li>
  </ul>

  <div class="brand-name"><span class="brand-dot"></span>Ridgeline Health Partners</div>

  <p class="salutation">Dear Sir / Madam,</p>

  <section class="letter-body">
    <p>Lorem ipsum dolor sit amet, consectetur adipisicing elit, sed do eiusmod tempor incididunt ut labore et dolore magna aliqua. Ut enim ad minim veniam, quis nostrud exercitation ullamco laboris nisi ut aliquip ex ea commodo consequa.Lorem ipsum dolor sit amet, consectetur adipisicing elit, sed do eiusmod tempor incididunt ut labore et dolore magna aliqua. Ut enim ad minim veniam, quis.</p>
    <p>Lorem ipsum dolor sit amet, consectetur adipisicing elit, sed do eiusmod tempor incididunt ut labore et dolore magna aliqua. Ut enim ad minim veniam, quis nostrud exercitation ullamco laboris nisi ut aliquip ex ea commodo consequa.Lorem ipsum dolor sit amet, consectetur adipisicing elit, sed do eiusmod tempor incididunt ut labore et dolore magna aliqua. Ut enim ad minim veniam, quis.</p>
    <p>Lorem ipsum dolor sit amet, consectetur adipisicing elit, sed do eiusmod tempor incididunt ut labore et dolore magna aliqua. Ut enim ad minim veniam, quis nostrud exercitation ullamco laboris nisi ut aliquip ex ea commodo consequa.Lorem ipsum dolor sit amet, consectetur adipisicing elit, sed do eiusmod tempor incididunt ut labore et dolore magna aliqua. Ut enim ad minim veniam, quis.</p>
    <p>Lorem ipsum dolor sit amet, consectetur adipisicing elit, sed do eiusmod tempor incididunt ut labore et dolore magna aliqua. Ut enim ad minim veniam, quis nostrud exercitation ullamco laboris nisi ut aliquip ex ea commodo consequa.Lorem ipsum dolor sit amet, consectetur adipisicing elit, sed do eiusmod tempor incididunt ut labore et dolore magna aliqua. Ut enim ad minim veniam, quis.</p>
    <p class="run-on">Lorem ipsum dolor sit amet, consectetur adipisicing elit, sed do eiusmod tempor incididunt ut labore et dolore magna aliqua. Ut enim ad minim veniam,</p>
  </section>

  <p class="sign-off">Best regards,<br>Yours Truly,</p>
  <p class="signature">Your Name</p>
  <p class="signer-title">Company Director</p>
</main>
</body>
</html>
```